Website Design

Hi I would like to invite designers to re design my website .

I would like the below in brief.

On the Welcome Page.

A nice looking technical page distributed into two

SALES on one side and TECHNOLOGY on the other . once the person clicks on either of them they can explore the pages in detail.

I am keen and almost ready with information for the Technology page and would like this to begin kicking ASAP .

my current website is www.plumvesta.net

Looking forward to seeing your feedback!

Oduya
Updates

Hi,

 
A little more elaboration on the web front page . I need it to be more techy .

I was looking at a wheel on the Technical side or a spanner and screew driver done on flash .

Just to give you a better idea on what seperated Sales from Technology. 

Sales 

Computing, Storage , Components , Peripherals , Software , TV & Gaming / Entertainment , Home & Leisure , Software , Gift Vouchers , Phones etc.

Technology .

Solar Power Solutions , Security Systems , Access Control , Automatic Gates & Turnstiles , Home/Office/Hotel Automation, Indoor and Outdoor PABX Telephony, Networking , Electricity Power Meters , IP Based Technology and ETC. 

See attached on the project updates my business card design if it can give you an idea ,also see revised Logo 

Industry/Entity Type

Sales

```html
<!DOCTYPE html>
<html lang="en">
<head>
<meta charset="utf-8">
<title>Plumvesta — Welcome</title>
<link rel="stylesheet" href="https://fonts.googleapis.com/css2?family=Roboto:wght@400;700&family=Oswald:wght@600&display=swap">
<style>
  :root {
    --page-bg: #eceef0;
    --page-glow: #fbfbfc;
    --brand-red: #d11b0c;
    --brand-red-dark: #b8170a;
    --nav-active: #2a2a2a;
    --nav-divider: #e2483a;
    --disc: #282828;
    --disc-label: #bdbdbd;
    --icon: #f4f4f4;
    --text: #222222;
    --rule: #dcdde0;
    --social-fill: #6d6d6d;
    --social-ring: #4a4a4a;
    --social-edge: #f5f5f5;
  }
  * { margin: 0; padding: 0; box-sizing: border-box; }
  html, body { width: 1200px; height: 675px; overflow: hidden; }
  body {
    position: relative;
    font-family: "Roboto", Arial, sans-serif;
    color: var(--text);
    background:
      radial-gradient(ellipse 360px 300px at 600px 330px, var(--page-glow) 0%, rgba(251,251,252,0) 100%),
      repeating-linear-gradient(90deg, rgba(255,255,255,0.35) 0 2px, rgba(0,0,0,0.012) 2px 5px),
      var(--page-bg);
  }
  .brand {
    position: absolute; left: 0; top: 30px; width: 1200px;
    text-align: center;
    font-size: 50px; font-weight: 700; letter-spacing: 1px;
    color: var(--brand-red);
  }
  .main-nav {
    position: absolute; left: 161px; top: 137px; width: 878px; height: 33px;
    background: var(--brand-red); border-radius: 4px;
  }
  .main-nav ul { list-style: none; position: absolute; left: 201px; top: 0; display: flex; height: 33px; }
  .main-nav li {
    display: flex; align-items: center; justify-content: center;
    height: 33px; font-size: 12.5px; color: #fff; text-transform: uppercase;
    border-right: 1px solid var(--nav-divider);
  }
  .main-nav li:last-child { border-right: none; }
  .main-nav li.is-active { background: var(--nav-active); border-right: none; }
  .section-links { position: absolute; left: 0; top: 0; }
  .section-link { position: absolute; width: 198px; height: 198px; }
  .section-link .disc {
    width: 198px; height: 198px; border-radius: 50%; background: var(--disc);
    display: flex; flex-direction: column; align-items: center;
  }
  .section-link svg { margin-top: 46px; }
  .section-link .label {
    font-family: "Oswald", "Arial Narrow", sans-serif; font-weight: 600;
    font-size: 20px; color: var(--disc-label); letter-spacing: -0.3px;
  }
  .section-link .floor-shadow {
    position: absolute; left: 47px; top: 222px; width: 104px; height: 10px;
    border-radius: 50%; background: rgba(0,0,0,0.28); filter: blur(4px);
  }
  .footer-rule { position: absolute; left: 161px; top: 530px; width: 878px; height: 1px; background: var(--rule); }
  .copyright {
    position: absolute; left: 0; top: 569px; width: 1200px; text-align: center;
    font-size: 11.5px;
  }
  .copyright .sep { margin: 0 12px; }
  .social { position: absolute; left: 545px; top: 610px; display: flex; gap: 9px; }
  .social span {
    width: 31px; height: 31px; border-radius: 50%;
    background: var(--social-fill); border: 2px solid var(--social-edge);
    box-shadow: 0 0 0 1px var(--social-ring);
  }
</style>
</head>
<body>
  <header>
    <div class="brand">Plumvesta</div>
    <nav class="main-nav">
      <ul>
        <li class="is-active" style="width:79px">Home</li>
        <li style="width:87px">About</li>
        <li style="width:85px">Sales</li>
        <li style="width:126px">Technology</li>
        <li style="width:94px">Contact</li>
      </ul>
    </nav>
  </header>

  <main class="section-links">
    <a class="section-link" style="left:351px; top:234px">
      <div class="disc">
        <svg width="72" height="72" viewBox="0 0 72 72" aria-hidden="true">
          <rect x="25" y="4" width="22" height="14" rx="5" fill="none" stroke="var(--icon)" stroke-width="5"/>
          <rect x="2" y="15" width="68" height="24" rx="6" fill="var(--icon)"/>
          <rect x="2" y="37" width="68" height="33" rx="6" fill="var(--icon)"/>
          <rect x="29" y="33" width="14" height="10" rx="2" fill="var(--disc)"/>
        </svg>
        <span class="label">SALES</span>
      </div>
      <div class="floor-shadow"></div>
    </a>
    <a class="section-link" style="left:650px; top:234px">
      <div class="disc">
        <svg width="72" height="72" viewBox="0 0 72 72" aria-hidden="true">
          <g fill="var(--icon)">
            <path d="M8 8 l10 10 l-5 5 l-10 -10 a16 16 0 0 0 20 18 l34 34 a5 5 0 0 0 8 -8 l-34 -34 a16 16 0 0 0 -18 -20 z"/>
            <path d="M66 4 l3 3 l-12 16 l-4 1 l-36 36 l-6 -6 l36 -36 l1 -4 z"/>
          </g>
        </svg>
        <span class="label">TECHNOLOGY</span>
      </div>
      <div class="floor-shadow"></div>
    </a>
  </main>

  <footer>
    <div class="footer-rule"></div>
    <p class="copyright">Copyright © <strong>Plumvesta</strong> 2013<span class="sep">I</span>Terms &amp; Conditions</p>
    <div class="social">
      <span role="img" aria-label="Social link"></span>
      <span role="img" aria-label="Social link"></span>
      <span role="img" aria-label="Social link"></span>
    </div>
  </footer>
</body>
</html>
```